Business Card Design for a Lending Business (Hard Money loans)

We need a business card for our Real Estate Lending business. We do hard Money loans for real estate investors. We have an existing logo we like, see attached. I'd like the business card to mostly include the logo colors, but a bright color pop of some sort would be nice to see also. Card should include Logo, Company Name, Company Address, Employee Name, Cell Phone, Main Phone, Email, Website

Industry/Entity Type

Finance / Lending

Contact Information for Business Card

Logo, Company Name, Company Address, Employee Name, Cell Phone, Main Phone, Email, Website

Requirements
Nice to have
• I'd like the business card to mostly include the logo colors, but a bright color pop of some sort would be nice to see also.

```html
<!DOCTYPE html>
<html lang="en">
<head>
<meta charset="utf-8">
<title>Kestrel Lending – Business Card</title>
<link rel="stylesheet" href="https://fonts.googleapis.com/css2?family=Montserrat:wght@600;700;800&family=Open+Sans:wght@400;600&display=swap">
<style>
  :root {
    --stage: #232323;
    --card-dark: #1f1f24;
    --navy: #283590;
    --navy-deep: #1c2470;
    --bright: #1aa3dc;
    --white: #ffffff;
  }
  * { box-sizing: border-box; margin: 0; padding: 0; }
  html, body {
    width: 1200px; height: 780px; overflow: hidden;
    background: var(--stage);
  }
  .stage {
    position: relative; width: 1200px; height: 780px;
  }
  .card {
    position: absolute; top: 70px; width: 380px; height: 640px;
    border: 2px solid var(--bright);
    overflow: hidden;
    box-shadow: 0 18px 40px rgba(0,0,0,.55);
  }
  /* back side */
  .card-back {
    left: 150px;
    border-radius: 180px 0 180px 0;
    background: var(--navy);
  }
  .card-back .pattern-field {
    position: absolute; inset: 0;
    background: linear-gradient(135deg, #3a6fb8 0%, #2c3f98 45%, #1c2470 100%);
  }
  .card-back .corner-brand {
    position: absolute; top: 36px; right: 30px;
    display: flex; align-items: center; gap: 8px;
    font-family: "Montserrat", sans-serif; font-weight: 700;
    font-size: 13px; letter-spacing: 1.5px; color: var(--white);
    text-transform: uppercase;
  }
  .corner-brand .brand-dot {
    width: 22px; height: 22px; border-radius: 50%;
    border: 2px solid var(--white);
  }
  /* front side */
  .card-front {
    left: 650px;
    border-radius: 0 180px 0 180px;
    background: var(--card-dark);
    font-family: "Open Sans", sans-serif;
    color: var(--white);
  }
  .brand {
    position: absolute; top: 110px; left: 0; right: 0;
    display: flex; flex-direction: column; align-items: center; gap: 14px;
  }
  .brand-mark {
    width: 74px; height: 74px; border-radius: 50%;
    background: var(--navy);
  }
  .brand-name {
    font-family: "Montserrat", sans-serif; font-weight: 800;
    font-size: 30px; letter-spacing: 4px; text-transform: uppercase;
    color: var(--navy); text-align: center; line-height: 1.15;
  }
  .person {
    position: absolute; top: 308px; left: 0; right: 0; text-align: center;
  }
  .person-name {
    font-family: "Montserrat", sans-serif; font-weight: 800; font-size: 30px;
  }
  .person-name .first { color: var(--navy); }
  .person-name .last { color: var(--bright); }
  .person-title { font-size: 15px; font-weight: 600; margin-top: 4px; }
  .contact-frame {
    position: absolute; top: 392px; left: 34px; width: 312px; height: 138px;
  }
  .contact-list {
    position: absolute; top: 426px; left: 0; right: 0;
    list-style: none; text-align: center;
    font-size: 15px; line-height: 23px;
  }
  .address {
    position: absolute; top: 548px; left: 0; right: 0; text-align: center;
    font-size: 15px; line-height: 21px;
  }
  .address svg { display: block; margin: 0 auto 6px; }
</style>
</head>
<body>
<main class="stage">

  <section class="card card-back" aria-label="Card back">
    <div class="pattern-field" role="img" aria-label="Repeating brand monogram pattern in blue tones"></div>
    <div class="corner-brand"><span class="brand-dot"></span>Kestrel Lending</div>
  </section>

  <section class="card card-front" aria-label="Card front">
    <div class="brand">
      <span class="brand-mark"></span>
      <span class="brand-name">Kestrel<br>Lending</span>
    </div>

    <div class="person">
      <p class="person-name"><span class="first">Marta</span> <span class="last">Kovalova</span></p>
      <p class="person-title">Director</p>
    </div>

    <svg class="contact-frame" viewBox="0 0 312 138" aria-hidden="true">
      <g fill="none" stroke="var(--bright)" stroke-width="2.5">
        <polyline points="60,30 4,30 4,128 48,128"/>
        <polyline points="252,30 308,30 308,110 286,110"/>
        <polyline points="80,48 36,48 36,60 48,60"/>
        <polyline points="232,48 276,48 276,60 266,60"/>
      </g>
      <g fill="var(--bright)">
        <polygon points="48,122 58,128 48,134"/>
        <polygon points="286,104 276,110 286,116"/>
        <polygon points="48,55 56,60 48,65"/>
        <polygon points="266,55 258,60 266,65"/>
        <circle cx="96" cy="30" r="15"/>
        <circle cx="136" cy="30" r="15"/>
        <circle cx="176" cy="30" r="15"/>
        <circle cx="216" cy="30" r="15"/>
      </g>
      <g fill="none" stroke="var(--white)" stroke-width="1.6">
        <rect x="89" y="25" width="14" height="10"/>
        <polyline points="89,25 96,31 103,25"/>
        <path d="M131,24 q0,-3 3,-2 l2,3 -2,2 q1,3 4,5 l2,-2 3,2 q1,3 -2,3 q-9,-2 -10,-11z"/>
        <rect x="172" y="22" width="8" height="15" rx="1.5"/>
        <circle cx="216" cy="30" r="7"/>
        <line x1="209" y1="30" x2="223" y2="30"/>
        <ellipse cx="216" cy="30" rx="3" ry="7"/>
      </g>
    </svg>

    <ul class="contact-list">
      <li>+001 303 555 0142</li>
      <li>+001 303 555 0187</li>
      <li>info@yourwebsite.com</li>
      <li>www.yourwebsite.com</li>
    </ul>

    <div class="address">
      <svg width="28" height="28" viewBox="0 0 28 28" aria-hidden="true">
        <circle cx="14" cy="14" r="14" fill="var(--bright)"/>
        <path d="M14,6 a5,5 0 0 1 5,5 c0,4 -5,9 -5,9 s-5,-5 -5,-9 a5,5 0 0 1 5,-5z" fill="none" stroke="var(--white)" stroke-width="1.6"/>
        <circle cx="14" cy="11" r="1.8" fill="var(--white)"/>
      </svg>
      <p>1850 Harbor Mill Road</p>
      <p>Fairhaven, CO 80000</p>
    </div>
  </section>

</main>
</body>
</html>
```